Solar WiFi Charging Bench

Sales Brochure using only the colors of the Tavenish Color Palette provided.
Municipal Government target customer.
Key Features are as follows:
LED Advertising display
Connection to internet (User Defined)
800W Solar
USB-A and USB-C cell phone charging ports
400ah battery backup with low voltage shutoff
Insulated for -40 Deg C
Wireless cell phone charging
Vandalism resistant.
Theft resistant

```html
<!DOCTYPE html>
<html lang="en">
<head>
<meta charset="utf-8">
<title>Solar WiFi Charging Bench – Tavenish Renewables</title>
<link rel="stylesheet" href="https://fonts.googleapis.com/css2?family=Anton&family=Archivo+Black&family=Mulish:wght@400;500;600&family=Montserrat:wght@500;600;700&display=swap">
<style>
  :root {
    --brand-blue: #3f52a6;
    --brand-cyan: #3ec6ef;
    --label-blue: #3c4fb2;
    --ink: #2b2b2b;
    --footer-dark: #353535;
    --page: #efefef;
    --paper: #ffffff;
    --dot: #24365f;
  }
  html, body {
    margin: 0;
    padding: 0;
    width: 1200px;
    height: 2766px;
    overflow: hidden;
    background: var(--page);
  }
  .flyer {
    position: absolute;
    left: 50px;
    top: 605px;
    width: 1100px;
    height: 1556px;
    background: var(--paper);
    overflow: hidden;
    box-shadow: 0 4px 18px rgba(0,0,0,0.12);
  }
  .flyer-art {
    position: absolute;
    left: 0;
    top: 0;
    width: 1100px;
    height: 1556px;
  }
  .brand {
    position: absolute;
    left: 64px;
    top: 70px;
    display: flex;
    align-items: center;
    gap: 14px;
    font-family: "Montserrat", sans-serif;
    font-weight: 600;
    color: var(--brand-blue);
  }
  .brand-dot {
    width: 22px;
    height: 22px;
    border-radius: 50%;
    background: var(--brand-blue);
  }
  .brand-name {
    font-size: 40px;
    line-height: 1;
    letter-spacing: 1px;
  }
  .brand-sub {
    display: block;
    font-size: 15px;
    letter-spacing: 4px;
    margin-top: 6px;
  }
  .title {
    position: absolute;
    left: 54px;
    top: 228px;
    margin: 0;
    color: #fff;
    line-height: 1;
  }
  .title-solar {
    display: block;
    font-family: "Anton", sans-serif;
    font-weight: 400;
    font-size: 92px;
    letter-spacing: 1px;
    line-height: 96px;
  }
  .title-bench {
    display: block;
    font-family: "Archivo Black", sans-serif;
    font-size: 62px;
    letter-spacing: 1px;
    line-height: 70px;
  }
  .features-heading {
    position: absolute;
    left: 338px;
    top: 518px;
    margin: 0;
    font-family: "Archivo Black", sans-serif;
    font-size: 48px;
    letter-spacing: 1px;
    color: var(--ink);
    line-height: 1;
  }
  .features-heading .accent { color: var(--brand-blue); }
  .feature {
    position: absolute;
    margin: 0;
    font-family: "Mulish", sans-serif;
    font-size: 27px;
    line-height: 33px;
    color: var(--ink);
    font-weight: 500;
  }
  .feature .accent { color: var(--label-blue); }
  .cta {
    position: absolute;
    left: 60px;
    top: 1462px;
    color: #fff;
    font-family: "Montserrat", sans-serif;
    line-height: 1;
  }
  .cta-top {
    display: block;
    font-size: 21px;
    font-weight: 600;
  }
  .cta-free {
    display: inline-block;
    font-size: 44px;
    font-weight: 700;
    vertical-align: bottom;
    margin-top: 4px;
  }
  .cta-rest {
    display: inline-block;
    font-size: 18px;
    font-weight: 600;
    line-height: 19px;
    vertical-align: bottom;
    margin-left: 4px;
  }
  .contact-phones {
    position: absolute;
    left: 462px;
    top: 1468px;
    color: #fff;
    font-family: "Montserrat", sans-serif;
    font-weight: 600;
    font-size: 30px;
    line-height: 35px;
  }
  .contact-web {
    position: absolute;
    left: 786px;
    top: 1470px;
    color: #fff;
    font-family: "Mulish", sans-serif;
    font-weight: 500;
    font-size: 20px;
    line-height: 29px;
  }
</style>
</head>
<body>
<main class="flyer">
  <svg class="flyer-art" viewBox="0 0 1100 1556" xmlns="http://www.w3.org/2000/svg">
    <defs>
      <linearGradient id="heroTone" x1="0" y1="0" x2="1" y2="1">
        <stop offset="0" stop-color="#5f7a4e"/>
        <stop offset="0.45" stop-color="#c9cfd8"/>
        <stop offset="1" stop-color="#6b5a48"/>
      </linearGradient>
      <linearGradient id="benchTone" x1="0" y1="0" x2="1" y2="1">
        <stop offset="0" stop-color="#d7d4cf"/>
        <stop offset="0.5" stop-color="#b9bec6"/>
        <stop offset="1" stop-color="#6f8a4a"/>
      </linearGradient>
    </defs>

    <!-- header -->
    <polygon class="title-band" points="0,199 485,199 604,497 0,497" fill="var(--brand-blue)"/>
    <polygon class="header-stripe" points="405,0 436,0 642,507 612,507" fill="var(--brand-blue)"/>
    <polygon class="hero-photo" role="img" aria-label="Photo of a woman sitting on the solar charging bench, looking at her phone, in a park"
             points="446,0 1100,0 1100,490 652,490" fill="url(#heroTone)"/>
    <rect class="hero-base" x="630" y="490" width="470" height="17" fill="var(--brand-blue)"/>

    <!-- key features bracket -->
    <polyline points="298,551 68,551 68,1390 298,1390" fill="none" stroke="var(--brand-blue)" stroke-width="2.5"/>
    <circle cx="298" cy="551" r="7" fill="var(--dot)"/>
    <circle cx="298" cy="1390" r="7" fill="var(--dot)"/>

    <!-- bench product photo -->
    <path d="M 406 1293 A 290 290 0 0 1 406 713" fill="none" stroke="var(--brand-blue)" stroke-width="6" transform="rotate(0)"/>
    <circle class="bench-photo" role="img" aria-label="Photo of the solar WiFi charging bench with curved canopy in front of a building" cx="406" cy="1003" r="282" fill="url(#benchTone)"/>

    <!-- feature ring -->
    <g class="feature-ring">
      <path d="M406,631 A372,372 0 0 1 533,653 L502,740 A280,280 0 0 0 406,723 Z" fill="var(--brand-blue)"/>
      <path d="M533,653 A372,372 0 0 1 645,718 L586,789 A280,280 0 0 0 502,740 Z" fill="var(--brand-cyan)"/>
      <path d="M645,718 A372,372 0 0 1 728,817 L648,863 A280,280 0 0 0 586,789 Z" fill="var(--brand-blue)"/>
      <path d="M728,817 A372,372 0 0 1 772,938 L682,954 A280,280 0 0 0 648,863 Z" fill="var(--brand-cyan)"/>
      <path d="M772,938 A372,372 0 0 1 772,1068 L682,1052 A280,280 0 0 0 682,954 Z" fill="var(--brand-blue)"/>
      <path d="M772,1068 A372,372 0 0 1 728,1189 L648,1143 A280,280 0 0 0 682,1052 Z" fill="var(--brand-cyan)"/>
      <path d="M728,1189 A372,372 0 0 1 645,1288 L586,1217 A280,280 0 0 0 648,1143 Z" fill="var(--brand-blue)"/>
      <path d="M645,1288 A372,372 0 0 1 533,1353 L502,1266 A280,280 0 0 0 586,1217 Z" fill="var(--brand-cyan)"/>
      <path d="M533,1353 A372,372 0 0 1 406,1375 L406,1283 A280,280 0 0 0 502,1266 Z" fill="var(--brand-blue)"/>
    </g>

    <!-- ring icons -->
    <g class="ring-icons" fill="none" stroke="#fff" stroke-width="3" stroke-linecap="round" stroke-linejoin="round">
      <!-- display -->
      <g transform="translate(463,682)">
        <rect x="-18" y="-13" width="36" height="22" fill="#fff" stroke="none"/>
        <line x1="0" y1="9" x2="0" y2="15"/><line x1="-9" y1="16" x2="9" y2="16"/>
      </g>
      <!-- cloud wifi -->
      <g transform="translate(569,721)">
        <path d="M-18,6 a9,9 0 0 1 4,-16 a12,12 0 0 1 22,2 a8,8 0 0 1 10,14 Z" fill="#fff" stroke="none"/>
        <path d="M-8,14 a11,11 0 0 1 16,0 M-4,19 a5,5 0 0 1 8,0" />
      </g>
      <!-- battery and plug -->
      <g transform="translate(656,793)">
        <rect x="-16" y="-14" width="14" height="28" rx="2"/>
        <line x1="-12" y1="-18" x2="-6" y2="-18"/>
        <path d="M-10,-6 l-3,7 h5 l-3,7"/>
        <path d="M4,-10 v8 h12 v-8 M7,-10 v-6 M13,-10 v-6 M10,-2 v16"/>
      </g>
      <!-- solar panel -->
      <g transform="translate(712,892)">
        <path d="M-18,6 L-12,-12 H18 L12,6 Z"/>
        <path d="M-15,-3 H15 M-6,-12 L-10,6 M4,-12 L0,6"/>
        <line x1="0" y1="6" x2="0" y2="14"/><line x1="-8" y1="15" x2="8" y2="15"/>
      </g>
      <!-- insulated house -->
      <g transform="translate(732,1003)">
        <path d="M-18,2 L-4,-10 L10,2 V14 H-18 Z"/>
        <rect x="-9" y="2" width="10" height="8"/>
        <path d="M14,-14 v10 M10,-10 l4,-4 l4,4 M12,6 l6,-8"/>
      </g>
      <!-- battery unit -->
      <g transform="translate(712,1114)">
        <rect x="-16" y="-16" width="22" height="32" rx="3"/>
        <circle cx="-5" cy="-6" r="2" fill="#fff"/>
        <line x1="-10" y1="8" x2="0" y2="8"/>
        <path d="M12,-12 v12 a4,4 0 0 1 -8,0"/>
      </g>
      <!-- wireless charging -->
      <g transform="translate(656,1213)">
        <path d="M2,-12 l-7,12 h7 l-4,12" stroke-width="3.5"/>
        <path d="M-12,-10 a16,16 0 0 0 0,20 M14,-10 a16,16 0 0 1 0,20 M-19,-15 a24,24 0 0 0 0,30 M21,-15 a24,24 0 0 1 0,30"/>
      </g>
      <!-- vandal resistant -->
      <g transform="translate(569,1285)">
        <rect x="-16" y="-16" width="32" height="32"/>
        <path d="M-8,-8 l16,16 M8,-8 l-16,16"/>
      </g>
      <!-- theft resistant -->
      <g transform="translate(463,1324)">
        <path d="M-14,-8 h20 l-3,-8 h-14 Z" fill="#fff" stroke="none"/>
        <circle cx="-4" cy="0" r="6"/>
        <path d="M-16,18 a12,12 0 0 1 22,0"/>
        <circle cx="12" cy="12" r="7"/>
        <line x1="7" y1="17" x2="17" y2="7"/>
      </g>
    </g>

    <!-- feature leaders -->
    <g class="leaders" fill="none" stroke="var(--dot)" stroke-width="2" stroke-dasharray="2 4">
      <polyline points="473,625 498,597 580,597"/>
      <polyline points="598,670 623,647 716,647"/>
      <polyline points="700,756 725,750 822,750"/>
      <polyline points="767,880 795,892 868,892"/>
      <polyline points="790,1003 873,1008"/>
      <polyline points="767,1134 795,1163 846,1163"/>
      <polyline points="700,1250 725,1270 779,1270"/>
      <polyline points="598,1336 623,1350 699,1350"/>
      <polyline points="473,1381 498,1404 580,1404"/>
    </g>
    <g class="leader-dots" fill="var(--dot)">
      <circle cx="473" cy="625" r="3"/><circle cx="580" cy="597" r="3.5"/>
      <circle cx="598" cy="670" r="3"/><circle cx="716" cy="647" r="3.5"/>
      <circle cx="700" cy="756" r="3"/><circle cx="822" cy="750" r="3.5"/>
      <circle cx="767" cy="880" r="3"/><circle cx="868" cy="892" r="3.5"/>
      <circle cx="790" cy="1003" r="3"/><circle cx="873" cy="1008" r="3.5"/>
      <circle cx="767" cy="1134" r="3"/><circle cx="846" cy="1163" r="3.5"/>
      <circle cx="700" cy="1250" r="3"/><circle cx="779" cy="1270" r="3.5"/>
      <circle cx="598" cy="1336" r="3"/><circle cx="699" cy="1350" r="3.5"/>
      <circle cx="473" cy="1381" r="3"/><circle cx="580" cy="1404" r="3.5"/>
    </g>

    <!-- footer -->
    <polygon class="footer-cta" points="0,1454 362,1454 405,1556 0,1556" fill="var(--brand-blue)"/>
    <polygon class="footer-contact" points="378,1458 1100,1458 1100,1556 420,1556" fill="var(--footer-dark)"/>
    <g class="contact-icons" fill="none" stroke="#fff" stroke-width="2.2" stroke-linecap="round" stroke-linejoin="round">
      <path d="M425,1474 c-3,3 -2,9 4,15 c6,6 12,7 15,4 l-4,-5 l-4,2 c-3,-2 -6,-5 -7,-8 l2,-4 Z"/>
      <rect x="760" y="1477" width="16" height="12" rx="1"/>
      <path d="M760,1478 l8,6 l8,-6"/>
      <circle cx="768" cy="1513" r="8"/>
      <path d="M760,1513 h16 M768,1505 c-4,5 -4,11 0,16 c4,-5 4,-11 0,-16"/>
    </g>
  </svg>

  <div class="brand">
    <span class="brand-dot"></span>
    <div class="brand-name">TAVENISH<span class="brand-sub">RENEWABLES</span></div>
  </div>

  <h1 class="title">
    <span class="title-solar">SOLAR WiFi</span>
    <span class="title-bench">CHARGING</span>
    <span class="title-bench">BENCH</span>
  </h1>

  <h2 class="features-heading"><span class="accent">KEY</span> FEATURES</h2>

  <p class="feature" style="left:591px; top:581px;"><span class="accent">LED Advertising</span> display</p>
  <p class="feature" style="left:727px; top:632px;"><span class="accent">Connection to internet<br>(User Defined)</span></p>
  <p class="feature" style="left:833px; top:716px;"><span class="accent">USB-A and</span><br>USB-C cell phone<br>charging ports</p>
  <p class="feature" style="left:878px; top:865px;"><span class="accent">Insulated for</span><br>-40 Deg C</p>
  <p class="feature" style="left:884px; top:993px;">800W Solar</p>
  <p class="feature" style="left:857px; top:1081px;"><span class="accent">400ah battery</span><br>backup with low<br>voltage shutoff</p>
  <p class="feature" style="left:790px; top:1222px;"><span class="accent">Wireless cell</span><br>phone charging</p>
  <p class="feature" style="left:710px; top:1333px;"><span class="accent">Vandalism</span> resistant.</p>
  <p class="feature" style="left:591px; top:1388px;"><span class="accent">Theft</span> resistant</p>

  <div class="cta">
    <span class="cta-top">GET YOUR</span>
    <span class="cta-free">FREE</span><span class="cta-rest">CONSULTATION<br>TODAY</span>
  </div>

  <div class="contact-phones">555.210.4471<br>555.389.0126</div>
  <div class="contact-web">sales@tavenishrenewables.com<br>www.tavenishrenewables.com</div>
</main>
</body>
</html>
```